LumaMove In-home Personal Training

I would like to have some eye-catching business card design. Opened to any ideas.

The business idea: mobile fitness - train clients at their places

Target Market(s)

General population, 20-60 years old

Industry/Entity Type

Fitness

Contact Information for Business Card

The information to include:
Name: Marta
Call or text: 306-555-0187
Website: LumaMove.ca
Please use the attached logo

Requirements
Should not have
• No orange or purple colours please

```html
<!DOCTYPE html>
<html lang="en">
<head>
<meta charset="utf-8">
<title>LumaMove Business Card</title>
<link href="https://fonts.googleapis.com/css2?family=Jost:wght@300;400&family=Arimo:wght@400;700&display=swap" rel="stylesheet">
<style>
  :root {
    --stage: #d9d9d9;
    --card: #ffffff;
    --ink: #2b2b2b;
    --ink-soft: #6a6a6a;
    --rule: #bdbdbd;
    --photo-dark: #6b5a50;
    --photo-mid: #b9aaa0;
    --photo-light: #eeeeee;
  }
  * { margin: 0; padding: 0; box-sizing: border-box; }
  html, body { width: 1200px; height: 802px; overflow: hidden; }
  body { background: var(--stage); position: relative; font-family: "Arimo", Arial, sans-serif; color: var(--ink); }

  .card {
    position: absolute; top: 274px; width: 442px; height: 265px;
    background: var(--card); border-radius: 14px; overflow: hidden;
    box-shadow: 2px 4px 8px rgba(0,0,0,0.3);
  }
  .card--front { left: 136px; }
  .card--back { left: 625px; }

  .brand-name {
    position: absolute; font-family: "Jost", sans-serif; font-weight: 300;
    color: var(--ink); letter-spacing: 2px; white-space: nowrap; text-align: center;
  }
  .brand-tagline {
    position: absolute; font-family: "Jost", sans-serif; font-weight: 400;
    color: var(--ink-soft); letter-spacing: 1.6px; white-space: nowrap; text-align: center;
    text-transform: uppercase;
  }

  .card--front .brand-name { left: 20px; width: 200px; top: 138px; font-size: 31px; }
  .card--front .brand-tagline { left: 20px; width: 200px; top: 178px; font-size: 6.5px; }

  .divider { position: absolute; left: 222px; top: 83px; width: 1px; height: 101px; background: var(--rule); }

  .contact { position: absolute; left: 245px; top: 85px; }
  .contact__name { font-weight: 700; font-size: 17px; letter-spacing: 0.5px; text-transform: uppercase; margin-bottom: 26px; }
  .contact__row { display: flex; align-items: center; gap: 4px; font-size: 14.5px; height: 16px; margin-bottom: 12px; }
  .contact__row svg { width: 15px; height: 15px; flex: none; }

  .photo-area {
    position: absolute; left: 0; top: 0; width: 340px; height: 265px;
    background: linear-gradient(90deg, var(--photo-dark) 0%, var(--photo-mid) 35%, var(--photo-light) 72%, rgba(255,255,255,0) 100%);
  }
  .card--back .brand-name { left: 210px; width: 220px; top: 178px; font-size: 42px; }
  .card--back .brand-tagline { left: 210px; width: 220px; top: 223px; font-size: 8px; }
</style>
</head>
<body>
  <section class="card card--front">
    <div class="brand-name">LumaMove</div>
    <div class="brand-tagline">In-home personal training</div>
    <div class="divider"></div>
    <div class="contact">
      <div class="contact__name">Marta</div>
      <div class="contact__row">
        <svg viewBox="0 0 16 16" fill="none" stroke="currentColor" stroke-width="1.4">
          <rect x="1" y="1" width="14" height="14" rx="2.5"/>
          <path d="M5 4.2l1.6-.4 1 2.2-1 .8c.5 1.2 1.4 2.1 2.6 2.6l.8-1 2.2 1-.4 1.6c-3.6.2-7-3.2-6.8-6.8z" stroke-linejoin="round"/>
        </svg>
        <span>306-555-0187</span>
      </div>
      <div class="contact__row">
        <svg viewBox="0 0 16 16" fill="none" stroke="currentColor" stroke-width="1.3">
          <circle cx="8" cy="8" r="6.6"/>
          <ellipse cx="8" cy="8" rx="3" ry="6.6"/>
          <path d="M1.4 8h13.2M2.5 4.6h11M2.5 11.4h11"/>
        </svg>
        <span>www.LumaMove.ca</span>
      </div>
    </div>
  </section>

  <section class="card card--back">
    <div class="photo-area" role="img" aria-label="Photo of a woman lifting dumbbells in a bright gym"></div>
    <div class="brand-name">LumaMove</div>
    <div class="brand-tagline">In-home personal training</div>
  </section>
</body>
</html>
```